3 banner themes for healthy foods supplements

Who you are
You are a top professional designer. You eat, sleep and breathe banners. You have them for breakfast, lunch and dinner. You have created so many high quality banners that you stopped counting.
Who we are
We are selling premium nutritional supplements.

Deliverables
We need to design 3 different banner themes, each in the following formats:
- Vertical rectangle: 240 x 400
- Mobile leaderboard: 320 x 50
- Banner: 468 x 60
- Leaderboard: 728 x 90
- Square: 250 x 250
- Small square: 200 x 200
- Large rectangle: 336 x 280
- Inline rectangle: 300 x 250
- Skyscraper: 120 x 600
- Wide skyscraper: 160 x 600
- Half-page: 300 x 600
- Large leaderboard: 970x90
- Large mobile banner: 320 x 100
- Billboard: 970 x 250
- Portrait: 300 x 1050

To give us a taste of your design skills, we invite you to submit one format (300 x 250) of each of the 3 different banner themes described below before we finally give you the green light and award you. Once awarded you should deliver all 3 themes with all above mentioned banner formats.

The final deliverable shall be editable .psd files.

Our products
The products we are advertising are organic, raw, vegan, premium nutritional supplements, such as algae powder, wheat grass powder and goji berries. The products stand to support a healthy life style. Please have a look at our shop. It is in German, but you get the gist. http://www.lumavera.-shop.example

The design
We would describe the style of the banners as follows:
- Premium
- Joyful
- White background
- Minimalistic

Each banner theme shall advertise the following messages about the products:
- Product name (chlorella algae powder , wheatgrass powder, goji berries)
- healthy
- 100 % vegan, raw and organic
- 100% natural
- premium product

Each of the above attributes can be represented with labels of different colours, similar to the attached sample files. We like the colour combination of the labels on this banner a lot.
All 3 themes shall contain our logo which you find attached to this job description. The logo shall be visible, but not too prominent.

The only difference between the 3 different themes shall be the product photo and the product name. All other elements on the banner shall be the same.

Theme A
This theme advertises algae powder, such as chlorella algae. The product photo is attached and should of course appear prominently on the banner.

Theme B
This theme advertises wheat grass powder. The product photo is attached and should of course appear prominently on the banner.

Theme C
This theme advertises goji berries. The product photo is attached and should of course appear prominently on the banner.

Target Market(s)

Health conscious people.

Industry/Entity Type

It Professional

Font styles to use
Sans Serif

Colors
00a990
a54499
f37122
fbed22
0692cd
9bcb3b
ffc214

Requirements
Must have
• - product image as per in the attachment
• - logo
• - bright, clear, joyful colors
Should not have
• - heavy dark colors
• - frame

```html
<!DOCTYPE html>
<html lang="en">
<head>
<meta charset="utf-8">
<title>Wheat Grass Powder – Banner Set</title>
<link rel="stylesheet" href="https://fonts.googleapis.com/css2?family=Arimo:ital,wght@0,400;0,700;1,700&display=swap">
<style>
  :root {
    --teal: #1f9f8b;
    --mint: #9fdcd3;
    --white: #ffffff;
    --gold: #ffc214;
    --purple: #a54499;
    --green: #9bcb3b;
    --blue: #0692cd;
    --orange: #f37122;
    --yellow: #fbed22;
    --button: #8cc13f;
    --ink: #333333;
    --powder: #b3b56f;
    --edge: #9a9a9a;
  }
  html, body {
    margin: 0;
    padding: 0;
    width: 1200px;
    height: 1200px;
    overflow: hidden;
    background: var(--white);
    font-family: "Arimo", Arial, sans-serif;
  }
  .canvas { position: relative; width: 1200px; height: 1200px; }
  .banner { position: absolute; display: block; outline: 1px solid var(--edge); }
  .banner--leaderboard { left: 99px; top: 78px; width: 1027px; height: 127px; }
  .banner--rectangle { left: 97px; top: 412px; width: 424px; height: 352px; }
  .banner--skyscraper { left: 895px; top: 294px; width: 226px; height: 846px; }
  .size-caption {
    position: absolute;
    margin: 0;
    font-size: 20px;
    color: var(--ink);
    transform: translateX(-50%);
  }
  .size-caption--leaderboard { left: 585px; top: 214px; }
  .size-caption--rectangle { left: 300px; top: 778px; }
  .size-caption--skyscraper { left: 1008px; top: 1158px; }

  .fill-teal { fill: var(--teal); }
  .fill-mint { fill: var(--mint); }
  .fill-white { fill: var(--white); }
  .fill-powder { fill: var(--powder); }
  .curve-gold { fill: none; stroke: var(--gold); stroke-width: 6; }
  .curve-purple { fill: none; stroke: var(--purple); stroke-width: 7; }
  .brand-dot { fill: var(--green); }
  .brand-name { fill: var(--ink); font-weight: 700; font-family: "Arimo", Arial, sans-serif; }
  .headline { fill: var(--ink); font-weight: 700; font-family: "Arimo", Arial, sans-serif; }
  .tag rect { stroke: rgba(255,255,255,.6); stroke-width: 1; }
  .tag--healthy rect { fill: var(--green); }
  .tag--vegan rect { fill: var(--blue); }
  .tag--natural rect { fill: var(--orange); }
  .tag--premium rect { fill: var(--yellow); }
  .tag text { font-family: "Arimo", Arial, sans-serif; font-weight: 700; font-style: italic; fill: var(--white); text-anchor: middle; }
  .tag--premium text { fill: var(--ink); }
  .shop-button rect { fill: var(--button); stroke: var(--white); stroke-width: 1.5; }
  .shop-button text { fill: var(--white); font-family: "Arimo", Arial, sans-serif; font-weight: 700; text-anchor: middle; }
</style>
</head>
<body>
<main class="canvas">

  <!-- Leaderboard 728 x 90 -->
  <svg class="banner banner--leaderboard" viewBox="0 0 728 90" preserveAspectRatio="none">
    <rect class="fill-white" width="728" height="90"/>
    <path class="fill-mint" d="M150,0 H236 C228,30 228,60 240,90 H128 C133,55 142,25 158,0 Z"/>
    <path class="curve-gold" d="M128,90 C133,55 142,25 158,0"/>
    <path class="fill-teal" d="M228,0 C300,10 360,40 380,90 H728 V0 Z"/>
    <path class="curve-purple" d="M228,0 C300,10 360,40 380,90"/>
    <g class="brand">
      <circle class="brand-dot" cx="20" cy="45" r="9"/>
      <text class="brand-name" x="34" y="51" font-size="16">Lumavera</text>
    </g>
    <g class="product-photo" role="img" aria-label="Pile of green wheat grass powder">
      <ellipse class="fill-powder" cx="285" cy="55" rx="42" ry="20"/>
    </g>
    <text class="headline" font-size="20">
      <tspan x="162" y="34">Wheat</tspan>
      <tspan x="142" y="55">Grass</tspan>
      <tspan x="130" y="75">Powder</tspan>
    </text>
    <g class="tag tag--healthy" transform="translate(405,25) rotate(-22)">
      <rect x="-55" y="-15" width="110" height="30"/>
      <text y="6" font-size="16">Healthy</text>
    </g>
    <g class="tag tag--vegan" transform="translate(450,40) rotate(-22)">
      <rect x="-75" y="-15" width="150" height="30"/>
      <text font-size="10.5"><tspan x="0" y="-2">100% Vegan, Raw,</tspan><tspan x="-20" y="10">&amp; Organic</tspan></text>
    </g>
    <g class="tag tag--natural" transform="translate(518,45) rotate(-22)">
      <rect x="-75" y="-15" width="150" height="30"/>
      <text y="6" font-size="17">100% Natural</text>
    </g>
    <g class="tag tag--premium" transform="translate(585,50) rotate(-22)">
      <rect x="-75" y="-15" width="150" height="30"/>
      <text y="4" font-size="12">Premium Product</text>
    </g>
    <g class="shop-button">
      <rect x="615" y="56" width="105" height="27" rx="4"/>
      <text x="667" y="74" font-size="13">SHOP NOW</text>
    </g>
  </svg>
  <p class="size-caption size-caption--leaderboard">728X90</p>

  <!-- Inline rectangle 300 x 250 -->
  <svg class="banner banner--rectangle" viewBox="0 0 300 250" preserveAspectRatio="none">
    <rect class="fill-teal" width="300" height="250"/>
    <path class="fill-white" d="M0,0 H300 V8 C240,42 120,57 0,62 Z"/>
    <path class="fill-white" d="M0,62 C60,60 120,55 172,45 C157,110 132,185 87,250 H0 Z"/>
    <path class="fill-mint" d="M0,62 C60,60 120,55 172,45 C163,90 153,130 142,168 C90,152 40,154 0,162 Z"/>
    <path class="curve-gold" d="M0,62 C120,57 240,42 300,8"/>
    <path class="curve-purple" d="M172,45 C157,110 132,185 87,250"/>
    <g class="brand">
      <circle class="brand-dot" cx="92" cy="30" r="8"/>
      <text class="brand-name" x="105" y="36" font-size="16">Lumavera</text>
    </g>
    <text class="headline" font-size="19">
      <tspan x="15" y="93">Wheat</tspan>
      <tspan x="28" y="112">Grass</tspan>
      <tspan x="35" y="131">Powder</tspan>
    </text>
    <g class="product-photo" role="img" aria-label="Pile of green wheat grass powder">
      <ellipse class="fill-powder" cx="42" cy="192" rx="52" ry="24"/>
    </g>
    <g class="tag tag--healthy" transform="translate(233,76) rotate(12)">
      <rect x="-45" y="-14" width="120" height="28"/>
      <text y="6" font-size="17">Healthy</text>
    </g>
    <g class="tag tag--vegan" transform="translate(208,110) rotate(12)">
      <rect x="-68" y="-18" width="170" height="36"/>
      <text font-size="12"><tspan x="0" y="-3">100% vegan, Raw</tspan><tspan x="-28" y="11">&amp; Organic</tspan></text>
    </g>
    <g class="tag tag--natural" transform="translate(203,156) rotate(12)">
      <rect x="-72" y="-18" width="180" height="36"/>
      <text y="7" font-size="19">100% Natural</text>
    </g>
    <g class="tag tag--premium" transform="translate(184,196) rotate(12)">
      <rect x="-80" y="-17" width="200" height="34"/>
      <text y="5" font-size="14">Premium Product</text>
    </g>
    <g class="shop-button">
      <rect x="100" y="213" width="105" height="27" rx="4"/>
      <text x="152" y="231" font-size="13">SHOP NOW</text>
    </g>
  </svg>
  <p class="size-caption size-caption--rectangle">300X250</p>

  <!-- Wide skyscraper 160 x 600 -->
  <svg class="banner banner--skyscraper" viewBox="0 0 160 600" preserveAspectRatio="none">
    <rect class="fill-teal" width="160" height="600"/>
    <path class="fill-white" d="M0,0 H160 V55 C120,85 60,95 0,97 Z"/>
    <path class="fill-white" d="M0,97 C60,95 120,85 160,55 V120 C150,200 100,280 0,322 Z"/>
    <path class="fill-mint" d="M0,97 C60,95 120,85 160,55 V120 C156,160 146,190 132,216 C90,206 40,206 0,212 Z"/>
    <path class="curve-gold" d="M0,97 C60,95 120,85 160,55"/>
    <path class="curve-purple" d="M160,120 C150,200 100,280 0,322"/>
    <g class="brand">
      <circle class="brand-dot" cx="42" cy="40" r="8"/>
      <text class="brand-name" x="55" y="46" font-size="16">Lumavera</text>
    </g>
    <text class="headline" font-size="21">
      <tspan x="12" y="130">Wheat</tspan>
      <tspan x="28" y="152">Grass</tspan>
      <tspan x="42" y="175">Powder</tspan>
    </text>
    <g class="product-photo" role="img" aria-label="Pile of green wheat grass powder">
      <ellipse class="fill-powder" cx="42" cy="236" rx="56" ry="26"/>
    </g>
    <g class="tag tag--healthy" transform="translate(98,340) rotate(15)">
      <rect x="-48" y="-16" width="130" height="32"/>
      <text y="7" font-size="18">Healthy</text>
    </g>
    <g class="tag tag--vegan" transform="translate(73,397) rotate(15)">
      <rect x="-100" y="-22" width="200" height="44"/>
      <text font-size="13"><tspan x="0" y="-3">100% vegan, Raw</tspan><tspan x="-32" y="13">&amp; Organic</tspan></text>
    </g>
    <g class="tag tag--natural" transform="translate(68,455) rotate(15)">
      <rect x="-100" y="-22" width="210" height="44"/>
      <text y="7" font-size="18">100% Natural</text>
    </g>
    <g class="tag tag--premium" transform="translate(74,510) rotate(15)">
      <rect x="-100" y="-22" width="210" height="44"/>
      <text y="5" font-size="14">Premium Product</text>
    </g>
    <g class="shop-button">
      <rect x="25" y="560" width="105" height="28" rx="4"/>
      <text x="77" y="579" font-size="13">SHOP NOW</text>
    </g>
  </svg>
  <p class="size-caption size-caption--skyscraper">160X600</p>

</main>
</body>
</html>
```